Modern Label for Loose Tea pouches on 4.5x6 Label

We need a new label for our teas that is very simple in design, but stylish and modern. This will be used to print labels for our loose tea pouches. The label will be at max 4.5x6 inches in size. There should be a place for the tea name, description, ingredients, and size that is changeable.
Preferably an AI file that allows me to setup variables to change the above items. There will also need to be our logo which is supplied, and our address on the label.
Address:
Brindle Teas
148 Lower Ferncliff Lane
Highland, NY 12097
Target Market(s)
Tea Lovers
Requirements
Must have
- Adobe Illustrator file with variables setup for replacement of tea name, description, ingredients, and size (weights 2oz, 4oz, 8oz, 1lb)

```html
<!DOCTYPE html>
<html lang="en">
<head>
<meta charset="utf-8">
<title>Brindle Teas – Loose Tea Labels</title>
<link rel="stylesheet" href="https://fonts.googleapis.com/css2?family=Fredoka:wght@600&family=Cookie&family=Crimson+Text:wght@400;700&display=swap">
<style>
  :root {
    --page-bg: #ffffff;
    --label-bg: #e9ebb6;
    --ink: #5e5e58;
    --body-ink: #66665c;
    --brand-pink: #e0388d;
    --ring: #8c9556;
    --white-tea: #f6f7ea;
    --black-tea: #8a8880;
    --green-tea: #c3c56f;
    --flower-tea: #df8fb1;
    --dash-white: #ffffff;
    --dash-black: #6a6a62;
    --dash-green: #9da35a;
    --dash-flower: #e0468f;
  }
  * { margin: 0; padding: 0; box-sizing: border-box; }
  html, body {
    width: 903px; height: 1200px; overflow: hidden;
    background: var(--page-bg);
  }
  .sheet { position: relative; width: 903px; height: 1200px; }

  .label {
    position: absolute;
    width: 415px; height: 557px;
    background: var(--label-bg);
    box-shadow: 2px 3px 6px rgba(0,0,0,0.25);
    text-align: center;
    color: var(--ink);
  }
  .label--white  { left: 25px;  top: 27px;  --dash: var(--dash-white);  --tea: var(--white-tea); }
  .label--black  { left: 461px; top: 27px;  --dash: var(--dash-black);  --tea: var(--black-tea); }
  .label--green  { left: 25px;  top: 610px; --dash: var(--dash-green);  --tea: var(--green-tea); }
  .label--flower { left: 461px; top: 610px; --dash: var(--dash-flower); --tea: var(--flower-tea); }

  .label__border {
    position: absolute; inset: 8px;
    border: 1px dashed var(--dash);
  }

  .brand { position: absolute; left: 0; right: 0; top: 12px; }
  .brand__dot {
    display: block; margin: 0 auto;
    width: 58px; height: 58px; border-radius: 50%;
    border: 3px solid var(--brand-pink);
    margin-top: 20px;
  }
  .brand__name {
    display: block; margin-top: 16px;
    font-family: "Crimson Text", serif; font-weight: 700;
    font-size: 32px; letter-spacing: 0.5px; line-height: 1;
    color: var(--brand-pink);
  }

  .tea-name {
    position: absolute; left: 0; right: 0; top: 152px;
    font-family: "Fredoka", sans-serif; font-weight: 600;
    font-size: 60px; line-height: 1; letter-spacing: 0.5px;
  }
  .tea-type {
    position: absolute; left: 0; right: 0; top: 220px;
    font-family: "Cookie", cursive;
    font-size: 46px; line-height: 1;
  }
  .ingredients {
    position: absolute; left: 35px; width: 350px; top: 272px;
    font-family: "Crimson Text", serif; font-size: 13.5px; line-height: 16px;
    text-align: left; color: var(--body-ink);
  }

  .emblem {
    position: absolute; left: 134px; top: 311px;
    width: 146px; height: 146px;
  }

  .size {
    position: absolute; left: 0; right: 0; top: 473px;
    font-family: "Crimson Text", serif; font-size: 11.5px; color: var(--body-ink);
  }
  .address {
    position: absolute; left: 0; right: 0; top: 497px;
    font-family: "Crimson Text", serif; font-size: 12px; line-height: 14.5px;
    font-style: normal; color: var(--body-ink);
  }
</style>
</head>
<body>
<main class="sheet">

  <section class="label label--white">
    <div class="label__border"></div>
    <div class="brand"><span class="brand__dot"></span><span class="brand__name">BRINDLE TEAS</span></div>
    <h1 class="tea-name">TEA NAME</h1>
    <h2 class="tea-type">White Tea</h2>
    <p class="ingredients">Ingredients: lorem ipsum dolor sit amet, consectetur adipisc-<br>ing elit. Etian egestas dignissim arcu et auctor.</p>
    <svg class="emblem" viewBox="0 0 146 146" role="img" aria-label="Round tea-leaf emblem on a white tea background">
      <circle cx="73" cy="73" r="71" fill="none" stroke="var(--ring)" stroke-width="3"/>
      <circle cx="73" cy="73" r="65" fill="var(--tea)"/>
    </svg>
    <p class="size">size 14oz</p>
    <address class="address">Brindle Teas<br>148 Lower Ferncliff Lane<br>Highland, NY 12097</address>
  </section>

  <section class="label label--black">
    <div class="label__border"></div>
    <div class="brand"><span class="brand__dot"></span><span class="brand__name">BRINDLE TEAS</span></div>
    <h1 class="tea-name">TEA NAME</h1>
    <h2 class="tea-type">Black Tea</h2>
    <p class="ingredients">Ingredients: lorem ipsum dolor sit amet, consectetur adipisc-<br>ing elit. Etian egestas dignissim arcu et auctor.</p>
    <svg class="emblem" viewBox="0 0 146 146" role="img" aria-label="Round tea-leaf emblem on a black tea background">
      <circle cx="73" cy="73" r="71" fill="none" stroke="var(--ring)" stroke-width="3"/>
      <circle cx="73" cy="73" r="65" fill="var(--tea)"/>
    </svg>
    <p class="size">size 14oz</p>
    <address class="address">Brindle Teas<br>148 Lower Ferncliff Lane<br>Highland, NY 12097</address>
  </section>

  <section class="label label--green">
    <div class="label__border"></div>
    <div class="brand"><span class="brand__dot"></span><span class="brand__name">BRINDLE TEAS</span></div>
    <h1 class="tea-name">TEA NAME</h1>
    <h2 class="tea-type">Green Tea</h2>
    <p class="ingredients">Ingredients: lorem ipsum dolor sit amet, consectetur adipisc-<br>ing elit. Etian egestas dignissim arcu et auctor.</p>
    <svg class="emblem" viewBox="0 0 146 146" role="img" aria-label="Round tea-leaf emblem on a green tea background">
      <circle cx="73" cy="73" r="71" fill="none" stroke="var(--ring)" stroke-width="3"/>
      <circle cx="73" cy="73" r="65" fill="var(--tea)"/>
    </svg>
    <p class="size">size 14oz</p>
    <address class="address">Brindle Teas<br>148 Lower Ferncliff Lane<br>Highland, NY 12097</address>
  </section>

  <section class="label label--flower">
    <div class="label__border"></div>
    <div class="brand"><span class="brand__dot"></span><span class="brand__name">BRINDLE TEAS</span></div>
    <h1 class="tea-name">TEA NAME</h1>
    <h2 class="tea-type">Flower Tea</h2>
    <p class="ingredients">Ingredients: lorem ipsum dolor sit amet, consectetur adipisc-<br>ing elit. Etian egestas dignissim arcu et auctor.</p>
    <svg class="emblem" viewBox="0 0 146 146" role="img" aria-label="Round tea-leaf emblem on a flower tea background">
      <circle cx="73" cy="73" r="71" fill="none" stroke="var(--ring)" stroke-width="3"/>
      <circle cx="73" cy="73" r="65" fill="var(--tea)"/>
    </svg>
    <p class="size">size 14oz</p>
    <address class="address">Brindle Teas<br>148 Lower Ferncliff Lane<br>Highland, NY 12097</address>
  </section>

</main>
</body>
</html>
```